Banner Design for High End Jewelry Website

We need a banner for our website (brindlestone.com) for a sale that we will be running. The banner should be a size 1187 × 400. I have included a few pieces of jewelry to be included in the banner (do not need to use all, can use just some). The banner should say:
"Christmas is Closer Than You Think Sale!"
Shop Now

Industry/Entity Type

Jewelry

```html
<!DOCTYPE html>
<html lang="en">
<head>
<meta charset="UTF-8">
<title>Christmas Is Near – Brindlestone</title>
<link href="https://fonts.googleapis.com/css2?family=Dancing+Script:wght@700&family=Montserrat:wght@300;800&display=swap" rel="stylesheet">
<style>
  :root {
    --red-deep: #c40008;
    --red-main: #e1040c;
    --red-bright: #ff2a1a;
    --glow: #ffd9a8;
    --white: #ffffff;
    --gold-light: #f0c860;
    --gold-mid: #d6a232;
    --gold-dark: #a8741a;
    --reflection: #f07a4a;
  }
  * { margin: 0; padding: 0; box-sizing: border-box; }
  html, body { width: 1200px; height: 404px; overflow: hidden; }
  body { background: var(--red-main); }

  .banner {
    position: relative;
    width: 1200px;
    height: 404px;
    overflow: hidden;
    background:
      radial-gradient(circle at 1010px 148px, var(--glow) 0, rgba(255,150,80,.7) 12px, rgba(255,60,30,.35) 60px, rgba(255,40,20,0) 200px),
      radial-gradient(ellipse at 60% 40%, var(--red-bright) 0%, var(--red-main) 45%, var(--red-deep) 100%);
  }

  .bracelet-photo {
    position: absolute;
    left: 40px; top: 0;
    width: 305px; height: 330px;
    border-radius: 48% 40% 40% 48% / 30% 30% 30% 30%;
    background: linear-gradient(120deg, var(--gold-light) 0%, var(--gold-mid) 50%, var(--gold-dark) 100%);
  }
  .ring-photo {
    position: absolute;
    left: 330px; top: 52px;
    width: 280px; height: 280px;
    border-radius: 50%;
    background: radial-gradient(circle at 60% 40%, #6f8a6a 0%, #5a4a5a 40%, var(--gold-mid) 75%, var(--gold-dark) 100%);
  }
  .jewelry-reflection {
    position: absolute;
    left: 40px; top: 330px;
    width: 520px; height: 74px;
    border-radius: 40% 40% 0 0;
    background: linear-gradient(180deg, var(--reflection) 0%, rgba(240,122,74,0) 100%);
    opacity: .8;
  }

  .headline {
    position: absolute;
    left: 760px; top: 88px;
    width: 400px;
    text-align: center;
    color: var(--white);
  }
  .headline-script {
    display: block;
    font-family: "Dancing Script", cursive;
    font-weight: 700;
    font-size: 82px;
    line-height: 92px;
  }
  .headline-bold {
    display: block;
    font-family: "Montserrat", sans-serif;
    font-weight: 800;
    font-size: 66px;
    line-height: 70px;
    letter-spacing: 1px;
  }
  .headline-light {
    display: block;
    font-family: "Montserrat", sans-serif;
    font-weight: 300;
    font-size: 33px;
    line-height: 46px;
  }
  .shop-button {
    position: absolute;
    left: 788px; top: 292px;
    width: 241px; height: 62px;
    border-radius: 9px;
    background: var(--white);
    color: var(--red-main);
    font-family: "Montserrat", sans-serif;
    font-weight: 800;
    font-size: 31px;
    line-height: 62px;
    text-align: center;
    text-decoration: none;
  }
</style>
</head>
<body>
  <div class="banner">
    <div class="bracelet-photo" role="img" aria-label="Gold scale-pattern cuff bracelet set with diamonds"></div>
    <div class="ring-photo" role="img" aria-label="Gold cluster ring with cabochon gemstones and a diamond band"></div>
    <div class="jewelry-reflection" role="img" aria-label="Reflection of the jewelry pieces"></div>

    <h1 class="headline">
      <span class="headline-script">Christmas</span>
      <span class="headline-bold">IS NEAR</span>
      <span class="headline-light">THAN YOU THINK!</span>
    </h1>
    <a class="shop-button" href="#">SHOP NOW</a>
  </div>
</body>
</html>
```